beauty salon

providing waxing services from a home base this must include which I will provide a price list and an address

Industry/Entity Type

Beauty Salon

Font styles to use
Script

Colors

Designer to choose colors to be used in the design.

```html
<!DOCTYPE html>
<html lang="en">
<head>
<meta charset="UTF-8">
<title>Danielle Beauty Therapy – Waxing Price List</title>
<link rel="stylesheet" href="https://fonts.googleapis.com/css2?family=Roboto+Condensed:wght@300;400;700&family=Lato:wght@400;700&family=Playball&display=swap">
<style>
  :root {
    --bg-dark: #1d121b;
    --bg-plum: #2c1a29;
    --pink: #e8197f;
    --magenta-deep: #8c0f6c;
    --magenta: #c2218f;
    --script-plum: #8e1468;
    --white: #ffffff;
    --band-light: #f4f2f3;
    --band-grey: #d9d6d8;
    --text-dark: #2a2228;
    --frame-grey: #b9b3b8;
  }
  * { box-sizing: border-box; margin: 0; padding: 0; }
  html, body { width: 1200px; height: 900px; overflow: hidden; background: var(--bg-dark); }
  .flyer {
    position: relative; width: 1200px; height: 900px; overflow: hidden;
    font-family: "Roboto Condensed", "Arial Narrow", sans-serif; color: var(--white);
  }
  .flyer-shapes { position: absolute; inset: 0; }
  .line { position: absolute; line-height: 1; white-space: nowrap; }

  .offer-line-1 { left: 29px; top: 72px; font-size: 40px; font-weight: 300; }
  .offer-line-1 .offer-percent { font-size: 74px; font-weight: 700; margin-right: 6px; }
  .offer-line-2 { left: 29px; top: 160px; font-size: 74px; font-weight: 400; color: var(--pink); }
  .offer-line-2 .offer-lead { font-weight: 300; }
  .offer-line-3 { left: 29px; top: 248px; font-size: 58px; font-weight: 300; }

  .therapist { right: 32px; text-align: right; }
  .therapist-role { top: 78px; font-size: 40px; font-weight: 300; }
  .therapist-name { top: 140px; font-size: 72px; font-weight: 400; color: var(--pink); }
  .therapist-diploma { top: 222px; font-size: 29px; font-weight: 400; color: var(--pink); }
  .therapist-field { top: 256px; font-size: 66px; font-weight: 300; }

  .service-label {
    position: absolute; top: 402px; height: 70px; display: flex; align-items: center; justify-content: center;
    font-family: "Playball", cursive; font-size: 44px; color: var(--script-plum);
  }
  .service-label--ladies { left: 0; width: 337px; }
  .service-label--mens { left: 871px; width: 329px; }

  .price-list { position: absolute; list-style: none; font-family: "Lato", sans-serif; font-size: 17.5px; line-height: 24px; }
  .price-list li { display: flex; justify-content: space-between; white-space: nowrap; }
  .price-list .item::before { content: "•"; margin-right: 6px; }
  .price-list .price { font-weight: 700; margin-left: 8px; }
  .price-list--ladies-face { left: 26px; top: 565px; width: 176px; }
  .price-list--ladies-body { left: 224px; top: 590px; width: 186px; }
  .price-list--mens { left: 980px; top: 568px; width: 200px; }
  .price-list--eyes { left: 778px; top: 654px; width: 170px; line-height: 30px; }
  .price-list--eyes .item::before { content: "•"; margin-right: 2px; }

  .eyes-heading { position: absolute; left: 782px; top: 614px; font-family: "Playball", cursive; font-size: 21px; white-space: nowrap; }

  .signature-block {
    position: absolute; left: 464px; top: 736px; width: 280px; text-align: center;
    font-family: "Playball", cursive; color: var(--script-plum); font-size: 22px; line-height: 27px;
  }
  .signature-block .signature-venue { display: block; margin-top: 2px; font-size: 15px; color: var(--text-dark); }

  .contact { position: absolute; font-family: "Lato", sans-serif; font-size: 18px; color: var(--text-dark); line-height: 24px; white-space: nowrap; }
  .contact-address { left: 51px; top: 815px; font-style: normal; }
  .contact-address .home-icon { position: absolute; left: -27px; top: 29px; }
  .contact-phone { left: 254px; top: 839px; display: flex; align-items: center; gap: 10px; }
  .contact-hours { right: 236px; top: 815px; text-align: right; font-size: 17px; }
  .contact-open { right: 18px; top: 815px; text-align: right; font-size: 17px; }
  .contact-open .open-title { font-weight: 700; color: var(--magenta-deep); font-size: 20px; }
</style>
</head>
<body>
<main class="flyer">
  <svg class="flyer-shapes" width="1200" height="900" viewBox="0 0 1200 900" aria-hidden="true">
    <defs>
      <linearGradient id="bgGrad" x1="0" y1="0" x2="1" y2="1">
        <stop offset="0" stop-color="#2a1a27"/>
        <stop offset="1" stop-color="#150d14"/>
      </linearGradient>
      <linearGradient id="panelGrad" x1="0" y1="0" x2="0" y2="1">
        <stop offset="0" stop-color="#c2218f"/>
        <stop offset="1" stop-color="#7f0e63"/>
      </linearGradient>
      <linearGradient id="bandGrad" x1="0" y1="0" x2="0" y2="1">
        <stop offset="0" stop-color="#ffffff"/>
        <stop offset="1" stop-color="#d9d6d8"/>
      </linearGradient>
      <linearGradient id="labelGrad" x1="0" y1="0" x2="0" y2="1">
        <stop offset="0" stop-color="#ffffff"/>
        <stop offset="1" stop-color="#e2dfe1"/>
      </linearGradient>
      <linearGradient id="frameGrad" x1="0" y1="0" x2="1" y2="1">
        <stop offset="0" stop-color="#d0279a"/>
        <stop offset="1" stop-color="#7a0d5f"/>
      </linearGradient>
      <linearGradient id="photoGrad" x1="0" y1="0" x2="1" y2="1">
        <stop offset="0" stop-color="#f1ddcf"/>
        <stop offset="0.5" stop-color="#e9c3a8"/>
        <stop offset="1" stop-color="#f8f1ea"/>
      </linearGradient>
    </defs>

    <rect class="backdrop" width="1200" height="900" fill="url(#bgGrad)"/>

    <polygon class="price-panel" points="0,519 410,519 606,690 800,519 1200,519 1200,793 0,793" fill="url(#panelGrad)"/>
    <polygon class="center-wedge" points="606,662 370,793 838,793" fill="#f6f4f5"/>

    <rect class="footer-band" x="0" y="793" width="1200" height="76" fill="url(#bandGrad)"/>
    <rect class="footer-stripe" x="0" y="869" width="1200" height="8" fill="var(--magenta)"/>

    <rect class="label-bar" x="0" y="402" width="337" height="70" fill="url(#labelGrad)"/>
    <rect class="label-bar" x="871" y="402" width="329" height="70" fill="url(#labelGrad)"/>

    <g class="hex-frame" transform="translate(606 333)">
      <polygon points="0,-301 250,-150 250,150 0,301 -250,150 -250,-150" fill="url(#frameGrad)"/>
      <polygon points="0,-287 238,-143 238,143 0,287 -238,143 -238,-143" fill="none" stroke="var(--frame-grey)" stroke-width="4"/>
      <polygon points="0,-276 229,-138 229,138 0,276 -229,138 -229,-138" fill="none" stroke="var(--frame-grey)" stroke-width="3"/>
      <g role="img" aria-label="Photo: smooth waxed legs with a pink lily flower">
        <polygon points="0,-266 221,-133 221,133 0,266 -221,133 -221,-133" fill="url(#photoGrad)"/>
      </g>
    </g>
  </svg>

  <div class="line offer-line-1"><span class="offer-percent">10%</span>DISCOUNT</div>
  <div class="line offer-line-2"><span class="offer-lead">on</span> FIRST</div>
  <div class="line offer-line-3">TREATMENT</div>

  <div class="line therapist therapist-role">BEAUTY THERAPIST:</div>
  <div class="line therapist therapist-name">DANIELLE</div>
  <div class="line therapist therapist-diploma">DIPLOMA OF BEAUTY</div>
  <div class="line therapist therapist-field">THERAPY</div>

  <div class="service-label service-label--ladies">Lady's Waxing</div>
  <div class="service-label service-label--mens">Men's Waxing</div>

  <ul class="price-list price-list--ladies-face">
    <li><span class="item">Eyebrow</span><span class="price">$8</span></li>
    <li><span class="item">Upper lip</span><span class="price">$8</span></li>
    <li><span class="item">Chin</span><span class="price">$8</span></li>
    <li><span class="item">Face wax</span><span class="price">$25</span></li>
    <li><span class="item">Bikini line</span><span class="price">$15</span></li>
    <li><span class="item">G string</span><span class="price">$20</span></li>
    <li><span class="item">½ Brazilian</span><span class="price">$30</span></li>
    <li><span class="item">Full Brazilian</span><span class="price">$40</span></li>
  </ul>

  <ul class="price-list price-list--ladies-body">
    <li><span class="item">Half arm</span><span class="price">$20</span></li>
    <li><span class="item">Upper half arm</span><span class="price">$20</span></li>
    <li><span class="item">Full arm</span><span class="price">$25</span></li>
    <li><span class="item">Half leg</span><span class="price">$15</span></li>
    <li><span class="item">Upper leg</span><span class="price">$20</span></li>
    <li><span class="item">¾ Leg</span><span class="price">$25</span></li>
    <li><span class="item">Full leg</span><span class="price">$35</span></li>
  </ul>

  <div class="eyes-heading">Eye Enhancement</div>
  <ul class="price-list price-list--eyes">
    <li><span class="item">Eyebrow tint</span><span class="price">$12</span></li>
    <li><span class="item">Eyelash tint</span><span class="price">$15</span></li>
  </ul>

  <ul class="price-list price-list--mens">
    <li><span class="item">Eyebrow</span><span class="price">$10</span></li>
    <li><span class="item">Half arm</span><span class="price">$20</span></li>
    <li><span class="item">Upper half arm</span><span class="price">$25</span></li>
    <li><span class="item">Full arm</span><span class="price">$30</span></li>
    <li><span class="item">Half leg</span><span class="price">$25</span></li>
    <li><span class="item">Full leg</span><span class="price">$45</span></li>
    <li><span class="item">Chest wax</span><span class="price">$40</span></li>
    <li><span class="item">Back wax</span><span class="price">$35</span></li>
  </ul>

  <p class="signature-block">Beauty Therapist: Danielle<br>Diploma of Beauty<br>Therapy<span class="signature-venue">at Mara Quinn</span></p>

  <address class="contact contact-address">
    <svg class="home-icon" width="18" height="16" viewBox="0 0 18 16" aria-hidden="true">
      <path d="M9 0 L18 8 L15.5 8 L15.5 16 L11 16 L11 11 L7 11 L7 16 L2.5 16 L2.5 8 L0 8 Z" fill="var(--magenta-deep)"/>
    </svg>
    12 Finch Lane<br>Hillcrest
  </address>

  <div class="contact contact-phone">
    <svg width="24" height="18" viewBox="0 0 24 18" aria-hidden="true">
      <path d="M2 6 C2 2 22 2 22 6 L22 8 L17 8 L17 6 L7 6 L7 8 L2 8 Z" fill="var(--text-dark)"/>
      <path d="M6 9 L18 9 L21 17 L3 17 Z" fill="var(--text-dark)"/>
      <circle cx="12" cy="13" r="2.2" fill="var(--band-light)"/>
    </svg>
    <span>0431 555 218</span>
  </div>

  <div class="contact contact-hours">Fridays 10am-7pm<br>Saturday 10am -4pm</div>
  <div class="contact contact-open"><span class="open-title">NOW OPEN:</span><br>Wednesday 10am – 4pm</div>
</main>
</body>
</html>
```